Business card for different employees

A professional new updated design incorporating our current business's color themes and styles such as our on-site service trucks decals included in pictures attached. Our current business card is very simple and not professionally designed. We are a small family business but want a professional corporate look.

Target Market(s)

Cards to be handed out to new customers , corperate meetings. For our on site service operators.

Industry/Entity Type

Hydraulic

Contact Information for Business Card

Address, website, phone number, email, logo.
slogan - "Industry chosen hose and fittings provider".
24/7 on-site service , supply and hose management
Experienced , indpendant , family owned

Font styles to use
Sans Serif

Requirements
Must have
• Easily editable so that I can add different names and different roles for employees etc.
Nice to have
• Freedom with colour doesn't necessarily have to be blue but that is our company colour theme with trucks and logo so makes sense for the card to have blue like the trucks.

```html
<!DOCTYPE html>
<html lang="en">
<head>
<meta charset="utf-8">
<title>Meridian Hose and Couplings – Business Card</title>
<link rel="stylesheet" href="https://fonts.googleapis.com/css2?family=Roboto:wght@400;700&family=Michroma&display=swap">
<style>
  :root {
    --backdrop: #b8b8b8;
    --ink-dark: #1b1b1b;
    --brand-blue: #1330b8;
    --paper: #ffffff;
  }
  html, body {
    margin: 0;
    padding: 0;
    width: 1200px;
    height: 801px;
    overflow: hidden;
    background: var(--backdrop);
    font-family: "Roboto", Arial, sans-serif;
  }
  .card {
    position: absolute;
    top: 274px;
    width: 443px;
    height: 263px;
    overflow: hidden;
  }

  /* Front */
  .card-front { left: 153px; background: var(--ink-dark); color: var(--paper); }
  .front-panel { position: absolute; left: 315px; top: 0; width: 128px; height: 263px; background: var(--brand-blue); }
  .front-disc {
    position: absolute; left: 186px; top: 2px; width: 258px; height: 258px;
    border-radius: 50%; background: var(--brand-blue);
  }
  .front-monogram {
    position: absolute; left: 186px; top: 2px; width: 258px; height: 258px;
    display: flex; align-items: center; justify-content: center;
    font-weight: 700; font-size: 54px; color: var(--paper); letter-spacing: 1px;
  }
  .person { position: absolute; left: 20px; top: 33px; }
  .person-name { font-size: 15.5px; font-weight: 700; color: var(--brand-blue); letter-spacing: .3px; margin: 0; line-height: 1.1; }
  .person-role { font-size: 13px; margin: 0; line-height: 1.2; }
  .address { position: absolute; left: 20px; top: 138px; font-size: 13px; line-height: 16px; margin: 0; font-style: normal; }
  .contacts { position: absolute; left: 20px; top: 184px; list-style: none; margin: 0; padding: 0; font-size: 13px; line-height: 16.5px; }
  .contacts li { display: flex; align-items: center; gap: 4px; }
  .contacts svg { width: 14px; height: 14px; flex: none; }

  /* Back */
  .card-back { left: 625px; background: var(--paper); }
  .brand-lockup { position: absolute; left: 45px; top: 48px; display: flex; align-items: center; gap: 12px; }
  .brand-dot { width: 74px; height: 74px; border-radius: 50%; background: var(--brand-blue); flex: none; }
  .brand-name { color: var(--brand-blue); font-weight: 700; line-height: 1; margin: 0; }
  .brand-name .big { display: block; font-size: 34px; letter-spacing: 3px; }
  .brand-name .small { display: block; font-size: 14.5px; letter-spacing: 3.2px; margin-top: 6px; }
  .slogan-band {
    position: absolute; left: 0; top: 150px; width: 100%; height: 35px;
    background: var(--ink-dark); color: var(--paper);
    font-family: "Michroma", "Roboto", sans-serif; font-size: 10.5px;
    display: flex; align-items: center; justify-content: center; padding-top: 3px; box-sizing: border-box;
  }
  .services-band {
    position: absolute; left: 0; top: 188px; width: 100%; height: 49px;
    background: var(--brand-blue); color: var(--paper);
    font-size: 13px; line-height: 16px; text-align: center;
    display: flex; flex-direction: column; justify-content: center;
  }
  .services-band p { margin: 0; }
</style>
</head>
<body>
  <section class="card card-front">
    <div class="front-panel"></div>
    <div class="front-disc"></div>
    <div class="front-monogram">MHC</div>

    <div class="person">
      <p class="person-name">DANIEL ARCHER</p>
      <p class="person-role">Managing Director</p>
    </div>

    <address class="address">421, Address line here<br>Country Name, 45452</address>

    <ul class="contacts">
      <li>
        <svg viewBox="0 0 24 24" aria-hidden="true"><path fill="#1330b8" d="M6.6 10.8a15.1 15.1 0 0 0 6.6 6.6l2.2-2.2c.3-.3.7-.4 1-.2 1.1.4 2.3.6 3.6.6.6 0 1 .4 1 1V20c0 .6-.4 1-1 1A17 17 0 0 1 3 4c0-.6.4-1 1-1h3.5c.6 0 1 .4 1 1 0 1.3.2 2.5.6 3.6.1.3 0 .7-.2 1z"/></svg>
        <span>0455 112 309</span>
      </li>
      <li>
        <svg viewBox="0 0 24 24" aria-hidden="true"><rect x="2" y="5" width="20" height="14" fill="#1330b8"/><path d="M2 5l10 8 10-8" fill="none" stroke="#1b1b1b" stroke-width="1.5"/></svg>
        <span>hello@meridianhose.example</span>
      </li>
      <li>
        <svg viewBox="0 0 24 24" aria-hidden="true"><g fill="none" stroke="#1330b8" stroke-width="1.6"><circle cx="12" cy="12" r="9.5"/><ellipse cx="12" cy="12" rx="4.5" ry="9.5"/><path d="M2.5 12h19M4 7h16M4 17h16"/></g></svg>
        <span>www.meridianhose.example</span>
      </li>
    </ul>
  </section>

  <section class="card card-back">
    <div class="brand-lockup">
      <div class="brand-dot"></div>
      <h1 class="brand-name"><span class="big">MERIDIAN</span><span class="small">HOSE AND COUPLINGS</span></h1>
    </div>
    <div class="slogan-band">INDUSTRY CHOSEN HOSE AND FITTINGS PROVIDER</div>
    <div class="services-band">
      <p>24/7 On-site Service &nbsp;|&nbsp; Supply and Hose Management</p>
      <p>Experienced, Indpendant, Family Owned</p>
    </div>
  </section>
</body>
</html>
```